The company Velquist needs a design for CBD capsules

We (Velquist) need a new design for our CBD capsules. We already have a design for CBD oil. However, we do not want to use this completely. The Talmbex label and the cans serve as a template. Please upload in the format 139mm x 59mm incl.
2mm bleed all around and in .pdf vector. The logo files for Velquist are included in the briefing.

Industry/Entity Type

Onlineshop

Colors
00AB8E
00BBA5
67D7C9
C6EFE9
E9F9F6

Requirements
Must have
• Please in the format 139mm x 59mm incl. 2mm bleed all around and .pdf vector
Should not have
• It shouldn't be the same label, but it should be recognizable.

```html
<!DOCTYPE html>
<html lang="de">
<head>
<meta charset="utf-8">
<title>Velquist CBD Kapseln – Etikett 139 × 59 mm</title>
<link rel="stylesheet" href="https://fonts.googleapis.com/css2?family=Montserrat:wght@500;600;700&family=Mrs+Saint+Delafield&display=swap">
<style>
  :root {
    --teal: #00ab8e;
    --teal-bright: #00bba5;
    --teal-soft: #67d7c9;
    --teal-pale: #c6efe9;
    --teal-mist: #e9f9f6;
    --ink: #0f4c45;
    --white: #ffffff;
    --backdrop: #dfe7e5;
  }
  * { margin: 0; padding: 0; box-sizing: border-box; }
  html, body {
    width: 1200px; height: 900px; overflow: hidden;
    background: var(--backdrop);
    font-family: "Montserrat", sans-serif;
    color: var(--ink);
  }
  .label {
    position: absolute; left: 30px; top: 208px;
    width: 1140px; height: 484px;
    background: var(--white);
    overflow: hidden;
  }
  .hemp-corner {
    position: absolute; top: 0; width: 70px; height: 130px;
    background: linear-gradient(160deg, var(--teal-soft), var(--teal));
    opacity: .75;
  }
  .hemp-corner--left { left: 0; border-radius: 0 0 70px 0; }
  .hemp-corner--right { right: 0; border-radius: 0 0 0 70px; }
  .brand {
    position: absolute; left: 0; right: 0; top: 24px;
    text-align: center;
    font-weight: 700; font-size: 76px; line-height: 1.1; letter-spacing: -1px;
    color: var(--teal);
  }
  .strength-tab {
    position: absolute; left: 0; top: 150px;
    width: 40px; height: 200px;
    background: var(--teal);
    border-radius: 0 14px 14px 0;
    display: flex; align-items: center; justify-content: center;
  }
  .strength-tab span {
    transform: rotate(-90deg);
    color: var(--white); font-weight: 700; font-size: 28px;
    white-space: nowrap;
  }
  .product-title {
    position: absolute; left: 330px; top: 128px;
    display: flex; align-items: baseline; gap: 20px;
  }
  .product-title .cbd { font-weight: 700; font-size: 96px; line-height: 1; }
  .product-title .type { font-weight: 500; font-size: 40px; }
  .title-rule {
    position: absolute; left: 330px; top: 236px;
    width: 480px; height: 3px; background: var(--teal-soft);
  }
  .claims {
    position: absolute; left: 330px; top: 248px;
    list-style: none;
  }
  .claims li {
    display: flex; align-items: center; gap: 10px;
    font-weight: 500; font-size: 36px; line-height: 50px;
  }
  .claims svg { width: 30px; height: 30px; flex: none; }
  .capsule-art {
    position: absolute; left: 840px; top: 130px;
    width: 200px; height: 220px;
    background: radial-gradient(ellipse at 50% 75%, var(--teal-soft) 0%, var(--teal-bright) 40%, rgba(0,187,165,0) 72%);
  }
  .base-band { position: absolute; left: 0; bottom: 0; width: 1140px; height: 120px; }
  .pack-info {
    position: absolute; left: 60px; top: 374px;
    width: 340px; height: 48px;
    border-top: 1.5px solid var(--teal-soft);
    border-bottom: 1.5px solid var(--teal-soft);
    display: flex; align-items: center; gap: 10px;
    padding-left: 8px;
    font-size: 28px; font-weight: 500;
  }
  .pack-info b { font-weight: 700; }
  .pack-info .divider { width: 1.5px; height: 38px; background: var(--teal-soft); margin-left: 6px; }
  .pack-info svg { width: 28px; height: 28px; }
  .spectrum {
    position: absolute; right: 50px; bottom: 34px;
    font-family: "Mrs Saint Delafield", cursive;
    font-size: 58px; line-height: 1; color: var(--white);
  }
</style>
</head>
<body>
  <main class="label">
    <div class="hemp-corner hemp-corner--left" role="img" aria-label="Hanfblatt-Illustration in der linken oberen Ecke"></div>
    <div class="hemp-corner hemp-corner--right" role="img" aria-label="Hanfblatt-Illustration in der rechten oberen Ecke"></div>

    <h1 class="brand">Velquist</h1>

    <div class="strength-tab"><span>10%</span></div>

    <h2 class="product-title"><span class="cbd">CBD</span><span class="type">Kapseln</span></h2>
    <div class="title-rule"></div>

    <ul class="claims">
      <li>
        <svg viewBox="0 0 34 34"><circle cx="16" cy="17" r="12" fill="none" stroke="var(--teal)" stroke-width="3.5"/><path d="M10 17l6 6L31 6" fill="none" stroke="var(--teal)" stroke-width="4" stroke-linecap="round" stroke-linejoin="round"/></svg>
        Vegan
      </li>
      <li>
        <svg viewBox="0 0 34 34"><circle cx="16" cy="17" r="12" fill="none" stroke="var(--teal)" stroke-width="3.5"/><path d="M10 17l6 6L31 6" fill="none" stroke="var(--teal)" stroke-width="4" stroke-linecap="round" stroke-linejoin="round"/></svg>
        Gentechnik Frei
      </li>
    </ul>

    <div class="capsule-art" role="img" aria-label="Hanfblatt mit grünen Softgel-Kapseln"></div>

    <svg class="base-band" viewBox="0 0 1140 120" aria-hidden="true">
      <rect x="0" y="86" width="1140" height="34" fill="var(--teal-soft)"/>
      <polygon points="700,0 1140,0 1140,120 640,120" fill="var(--teal)"/>
    </svg>

    <div class="pack-info">
      <span><b>39</b>g <b>60</b> Kapseln</span>
      <span class="divider"></span>
      <svg viewBox="0 0 30 30"><g transform="rotate(-45 15 15)" fill="none" stroke="var(--ink)" stroke-width="1.8"><rect x="3" y="10" width="24" height="10" rx="5"/><line x1="15" y1="10" x2="15" y2="20"/></g></svg>
    </div>

    <p class="spectrum">Vollspektrum</p>
  </main>
</body>
</html>
```